Business Card Design Project

I need a business card design for our new logo, please check the logo at the following link:
https://files.quorvane-share.com/s/p7tkwe3nq4zr81h/FernCove.png
The address on the business card:
Av. Olegário Tavares 418 sala 207
Barra da Tijuca, Rio de Janeiro, RJ
CEP: 24917-380
Brasil
Phone: +55 21 73408216
e-mail: rogerio@ferncove-exemplo.com.br
Updates
Thank you all for sending your designs, we will not provide feedback because there are too many designs, on December 3 we will pick the best design according to our point of view. Please keep posting.
Rogério
Industry/Entity Type
Business

```html
<!DOCTYPE html>
<html lang="pt-BR">
<head>
<meta charset="utf-8">
<title>FernCove – Business Card</title>
<link rel="stylesheet" href="https://fonts.googleapis.com/css2?family=Arimo:ital,wght@0,400;0,700;1,400&display=swap">
<style>
  :root {
    --backdrop: #fbb455;
    --card-dark: #1e1e1e;
    --brand-yellow: #f6c500;
    --badge-white: #ffffff;
    --text-font: "Arimo", Arial, sans-serif;
  }
  * { margin: 0; padding: 0; box-sizing: border-box; }
  html, body {
    width: 1200px; height: 1000px; overflow: hidden;
    background: var(--backdrop);
    font-family: var(--text-font);
  }
  .canvas { position: relative; width: 1200px; height: 1000px; }

  .card {
    position: absolute;
    width: 798px; height: 443px;
    background: var(--card-dark);
    overflow: hidden;
  }
  .card--front { left: 47px; top: 42px; }
  .card--back  { left: 351px; top: 511px; }

  .front-ring { position: absolute; inset: 0; }

  .brand-badge {
    position: absolute;
    width: 237px; height: 150px;
    border-radius: 75px;
    background: var(--badge-white);
    display: flex; align-items: center; justify-content: center;
    gap: 10px;
  }
  .card--front .brand-badge { left: 73px; top: 40px; }
  .card--back .brand-badge { left: 283px; top: 145px; height: 149px; }

  .brand-dot {
    width: 18px; height: 18px; border-radius: 50%;
    background: var(--brand-yellow);
  }
  .brand-name {
    font-family: var(--text-font);
    font-weight: 700;
    font-size: 28px;
    color: var(--card-dark);
    letter-spacing: -0.3px;
  }

  .contact {
    position: absolute;
    left: 514px;
    color: var(--brand-yellow);
    font-size: 14.5px;
    line-height: 22.7px;
  }
  .contact--address { top: 185px; font-style: normal; }
  .contact--reach { top: 320px; }
  .contact-label { font-style: italic; }

  .back-band {
    position: absolute;
    left: 0; top: 145px;
    width: 100%; height: 149px;
    background: var(--brand-yellow);
  }
</style>
</head>
<body>
<main class="canvas">
  <section class="card card--front" aria-label="Business card front">
    <svg class="front-ring" width="798" height="443" viewBox="0 0 798 443" aria-hidden="true">
      <circle cx="659" cy="263" r="302" fill="var(--brand-yellow)"/>
      <circle cx="659" cy="263" r="242" fill="var(--card-dark)"/>
    </svg>

    <div class="brand-badge">
      <span class="brand-dot"></span>
      <span class="brand-name">FernCove</span>
    </div>

    <address class="contact contact--address">
      Av. Olegário Tavares 418 sala 207<br>
      Barra da Tijuca, Rio de Janeiro, RJ<br>
      CEP: 24917-380<br>
      Brasil
    </address>

    <p class="contact contact--reach">
      <span class="contact-label">Phone:</span> +55 21 73408216<br>
      <span class="contact-label">e-mail:</span> rogerio@ferncove-exemplo.com.br
    </p>
  </section>

  <section class="card card--back" aria-label="Business card back">
    <div class="back-band"></div>
    <div class="brand-badge">
      <span class="brand-dot"></span>
      <span class="brand-name">FernCove</span>
    </div>
  </section>
</main>
</body>
</html>
```